High end boutique food product label

We are looking for a label design to be used on our range of high end food products. We don't have a design or colour scheme in mind and are interested to see what ideas are submitted.
We would like it to feel sophisticated, chic, and eye-catching.
All of our products are handmade in Australia using Australian ingredients.
The graphics for the label will need to be scaleable to be fit a variety of labels from small squat jars with labels sized 3.5cm high and 7cm wide, to tall thin bottles with labels that are 14cm high and 4.5cm wide.
We would be interested in working with the winning designer to create these different sized labels.
The label submitted for this project should be 14cm high and 4.5cm wide, it should include our logo (file supplied in .jpeg and .ai), the product name 'Extra Virgin Olive Oil' and the size '250ml'.
This is just the front label on a bottle, we are not expecting a rear label to be created currently.
You are welcome to use any fonts you think will look good but the fonts used in our logo are Allaina Medium and Bebas Kai Regular.

```html
<!DOCTYPE html>
<html lang="en">
<head>
<meta charset="utf-8">
<title>Extra Virgin Olive Oil – Front Label</title>
<link rel="stylesheet" href="https://fonts.googleapis.com/css2?family=Bebas+Neue&family=Montserrat:wght@600&display=swap">
<style>
  :root {
    --page: #ffffff;
    --label-bg: #ffffff;
    --label-edge: #1c1a1a;
    --ink-dark: #231b18;
    --green-deep: #3f9a2a;
    --green-mid: #4caf38;
    --green-light: #a6f58a;
    --green-pill: #45bb2e;
    --white: #ffffff;
    --oil-gold: #e9b923;
    --olive: #6c9a25;
  }
  * { margin: 0; padding: 0; box-sizing: border-box; }
  html, body {
    width: 1200px;
    height: 2796px;
    overflow: hidden;
    background: var(--page);
  }
  .canvas {
    position: relative;
    width: 1200px;
    height: 2796px;
  }
  .label {
    position: absolute;
    left: 171px;
    top: 70px;
    width: 858px;
    height: 2656px;
    background: var(--label-bg);
    border: 3px solid var(--label-edge);
  }
  .brand-name {
    position: absolute;
    left: 0;
    right: 0;
    top: 250px;
    text-align: center;
    font-family: "Bebas Neue", sans-serif;
    font-size: 118px;
    line-height: 1;
    letter-spacing: 2px;
    color: var(--ink-dark);
  }
  .brand-name span { display: block; }
  .title-band {
    position: absolute;
    left: 31px;
    top: 781px;
    width: 787px;
    height: 960px;
  }
  .title-band svg { display: block; width: 100%; height: 100%; }
  .product-name {
    position: absolute;
    left: 0;
    right: 0;
    top: 352px;
    text-align: center;
    color: var(--white);
  }
  .product-name .grade {
    display: block;
    font-family: "Bebas Neue", sans-serif;
    font-size: 124px;
    line-height: 0.9;
    letter-spacing: 1px;
  }
  .product-name .variety {
    display: block;
    font-family: "Montserrat", sans-serif;
    font-weight: 600;
    font-size: 132px;
    line-height: 1;
    letter-spacing: 1px;
  }
  .product-visual {
    position: absolute;
    left: 147px;
    top: 1813px;
    width: 584px;
    height: 570px;
    border-radius: 44% 44% 40% 40% / 30% 30% 46% 46%;
    background: radial-gradient(ellipse at 45% 75%, var(--oil-gold) 0%, #f3dc7a 32%, #eef3e2 60%, var(--page) 78%),
                linear-gradient(90deg, transparent 60%, rgba(108,154,37,0.35) 100%);
  }
  .volume-tag {
    position: absolute;
    left: 258px;
    bottom: -3px;
    width: 336px;
    height: 104px;
    background: var(--green-pill);
    border-radius: 18px 18px 0 0;
    color: var(--white);
    font-family: "Bebas Neue", sans-serif;
    font-size: 84px;
    line-height: 110px;
    text-align: center;
  }
</style>
</head>
<body>
  <main class="canvas">
    <section class="label">
      <h1 class="brand-name"><span>Hollow Creek</span><span>Provisions</span></h1>

      <div class="title-band">
        <svg viewBox="0 0 787 960" preserveAspectRatio="none" aria-hidden="true">
          <defs>
            <linearGradient id="bandGreen" x1="0" y1="0" x2="0" y2="1">
              <stop offset="0" stop-color="var(--green-mid)"/>
              <stop offset="0.28" stop-color="var(--green-light)"/>
              <stop offset="0.52" stop-color="var(--green-mid)"/>
              <stop offset="0.75" stop-color="#47a932"/>
              <stop offset="0.9" stop-color="var(--green-deep)"/>
              <stop offset="1" stop-color="var(--green-light)"/>
            </linearGradient>
          </defs>
          <path fill="url(#bandGreen)" d="
            M0 80 L49 0 L98 80 L147 0 L196 80 L246 0 L295 80 L344 0 L393 80
            L443 0 L492 80 L541 0 L590 80 L640 0 L689 80 L738 0 L787 80
            L787 880 L738 960 L689 880 L640 960 L590 880 L541 960 L492 880
            L443 960 L393 880 L344 960 L295 880 L246 960 L196 880 L147 960
            L98 880 L49 960 L0 880 Z"/>
        </svg>
        <h2 class="product-name">
          <span class="grade">Extra Virgin</span>
          <span class="variety">OLIVE OIL</span>
        </h2>
      </div>

      <div class="product-visual" role="img" aria-label="Illustration of a glass jug of golden olive oil with green olives and leaves"></div>

      <p class="volume-tag">250ML</p>
    </section>
  </main>
</body>
</html>
```